Tarno Booking website (www.tarnobooking.example)

My company develops booking software, Tarno Booking, for the hourly booking of resources such as classes in a school or customer booking involving rooms in a spa. These bookings also involve the customers, staff, rooms and a lesson or treatment.

The main difference between this software and general calendar software such as Plexo calendar is that this Tarno Booking allows resources such as people and rooms to be associated with the bookings. This is important for example in the case of a Spa to make sure the rooms are booked appropriately and to see the free times for the rooms. For a golf practice range the players much be booked to the tee spots where they practice golf.

I have tried to design the website myself, as a computer programmer- I am a bit "square" and not a designer, my first attempt is http://www.tarnobooking.example/, my second attempt is at http://www.quenbel-works.example/tarnobookingwebsite/
I am not happy with my designs as compared to the professional designs I see people can come up with here. The software must have the image of a professional software product in order to inspire the confidence of customers.

Am looking for a design which will be the most likely to give the customer the following feeling:
* Confident the product can do the job.
* Feel easy to want to try it, at least for the free trial.
* Its a professional software product and also a web based product, the user can login from the web.

Look at other booking software websites for ideas, here is a list of links to similar booking products. These products all have different features but are mostly for resource booking.
http://quenbel-works.example/tarnobookingwebsite/?page=compare

Hello all,

Thankyou for the designs so far, to save peoples time, I will try to eliminate the bottom 50% of designs now.

To be honest, most of the designs are of a good or high quality, I think its very tough on you as graphic and web designers. Only a minor few are of low quality.

If your design is discarded - I would say its unlikely that you are going to be able to produce a design that will beat the competition. 
You probably already know, you could try to re-sell your design later for other projects or as a template on one of those template websites. Some of these discarded designs are quite worthwhile designs.

Best regards, Dorian

Target Market(s)

Spa, Gym, School, Golf, any organization who manages bookings of their customers

Industry/Entity Type

Software

Requirements
Must have
• Home page and inner page, any other pages up to you.

Make a logo or use the image of the girl that I already have on the second design.

Menu(s) for navigation.

A language switcher for 3 languages, English, Chinese Traditional and Chinese Simplified. (Western, Hong Kong and Chinese mainland market are important).

Space for a video introduction, it could be small and when the user clicks on it then it gets bigger then it won't take up too much space. Up to you.

A space for the user to login and register a new account.

Screenshots.

I don't have any strong preferences, use your own ideas, if you look at all the other products you can get the basic idea from them.

The total goal is to make a website which is going to lead to sales of the software product.

```html
<!DOCTYPE html>
<html lang="en">
<head>
<meta charset="utf-8">
<title>Tarno Booking</title>
<link href="https://fonts.googleapis.com/css2?family=Oswald:wght@400&family=Noto+Sans:wght@400;700&display=swap" rel="stylesheet">
<style>
:root{
  --red:#d3191b;
  --red-dark:#a80d0f;
  --red-text:#b01010;
  --ink:#1c1c1c;
  --body:#444;
  --grey-bg:#f3f3f3;
  --panel:#eaeaea;
  --footer:#262626;
  --footer-text:#e6e6e6;
}
*{box-sizing:border-box;margin:0;padding:0}
html,body{width:1029px;height:1200px;overflow:hidden}
body{position:relative;background:var(--grey-bg);font-family:"Noto Sans",sans-serif;color:var(--body);font-size:11.5px;line-height:1.3}
.abs{position:absolute}
.heading{font-family:"Oswald",sans-serif;font-weight:400;color:var(--ink)}

/* top bar */
.topbar{left:0;top:0;width:1029px;height:38px;background:linear-gradient(#c81416,#b00d10);border-bottom:1px solid #8c0a0c}
.lang{left:103px;top:8px;width:157px;height:22px;background:#fff;border:1px solid #ccc;font-size:10px;padding:3px 8px;color:#555}
.lang::after{content:"";position:absolute;right:0;top:0;width:20px;height:20px;border-left:1px solid #ddd;background:#f4f4f4}
.lang-caret{position:absolute;right:6px;top:8px;border:4px solid transparent;border-top-color:#888}
.field{top:8px;height:22px;background:#fff;border:1px solid #ddd;border-radius:3px;font-size:10px;padding:4px 7px;color:#999}
.btn{top:7px;height:24px;border-radius:3px;color:#fff;font-weight:700;font-size:10.5px;text-align:center;line-height:24px}
.btn-login{left:778px;width:94px;background:linear-gradient(#444,#111)}
.btn-signup{left:855px;width:70px;background:linear-gradient(#e52a2a,#b30f12);border:1px solid #8c0a0c;left:856px}

/* header */
.header{left:0;top:38px;width:1029px;height:95px;background:linear-gradient(#fafafa,#e2e2e2)}
.logo{left:103px;top:60px;display:flex;align-items:center;gap:8px}
.logo-mark{width:40px;height:40px;background:var(--red)}
.logo-name{font-family:"Oswald",sans-serif;font-size:26px;color:#333}
.nav{left:310px;top:63px;display:flex;font-size:14.5px;color:#222}
.nav span{padding:10px 18px;border-right:1px solid #ccc}
.nav span:first-child{padding-left:18px}
.nav span:last-child{border-right:none;padding-right:0}

/* hero */
.hero{left:0;top:133px;width:1029px;height:333px;background:radial-gradient(ellipse at 45% 40%,#e5231f,#c2130f 60%,#9d0b0b)}
.hero-title{left:102px;top:180px;font-size:34px;color:#fff}
.hero-copy{left:104px;top:236px;width:320px;color:#fff;font-size:11.8px;line-height:1.25}
.hero-note{left:107px;top:304px;color:#fff;font-size:15px}
.cta{left:104px;top:350px;width:311px;height:59px;border-radius:30px;background:linear-gradient(#fff,#d8d8d8);box-shadow:0 2px 4px rgba(0,0,0,.35);font-family:"Oswald",sans-serif;color:var(--red);font-size:20px;text-align:center;line-height:59px}
.video{left:455px;top:160px;width:471px;height:264px;background:#000;border:1px solid #ddd}
.video-play{left:213px;top:108px}
.video-bar{left:0;bottom:0;width:100%;height:22px;background:#eee;border-top:1px solid #ccc;font-size:8.5px;color:#333}
.track{left:28px;top:8px;width:364px;height:6px;border:1px solid #bbb;border-radius:3px;background:#fafafa}
.track i{position:absolute;left:0;top:0;width:58px;height:4px;background:#ccc;border-radius:3px}
.knob{left:80px;top:5px;width:12px;height:12px;border-radius:50%;background:#fff;border:1px solid #999}

/* features */
.feature{top:490px;width:265px}
.feature-icon{position:absolute;left:0;top:4px;width:43px;height:43px;border-radius:6px}
.feature-title{position:absolute;left:56px;top:11px;font-size:20px;white-space:nowrap}
.feature-text{position:absolute;left:0;top:56px;width:265px;font-size:11.8px;line-height:1.22}
.feature-text ul{list-style:none;font-size:9.6px;line-height:1.5;margin-top:2px}
.feature-text li::before{content:"• ";color:var(--red)}
.rule{left:160px;top:703px;width:720px;height:1px;background:linear-gradient(90deg,transparent,#ccc,transparent)}

/* tour & news */
.section-title{font-size:29px}
.section-title em{font-style:normal;color:var(--red-text)}
.tour{left:103px;top:776px;width:532px;height:197px;background:var(--panel)}
.shot{top:21px;width:206px;height:156px;background:#fff;font-size:17px;color:#777;text-align:center;line-height:156px}
.arrow{top:70px;width:30px;height:56px;background:#f8f8f8;border-radius:28px}
.news{left:661px;width:265px}
.news-date{font-size:9.5px;color:#888}
.news-title{font-weight:700;color:#222;font-size:11.8px;margin-top:2px}
.news-body{font-size:11.8px;line-height:1.4;color:#444}
.news-body b{font-weight:400;color:var(--red-text)}
.dots{left:661px;top:863px;width:265px;border-top:1px dotted #777}

/* footer */
.footer{left:0;top:1017px;width:1029px;height:183px;background:var(--footer);color:var(--footer-text)}
.foot-logo{left:103px;top:1040px;display:flex;align-items:center;gap:7px}
.foot-logo .logo-mark{width:34px;height:34px}
.foot-logo .logo-name{color:#ddd;font-size:22px}
.foot-copy{left:104px;top:1093px;font-size:11.8px;color:var(--footer-text)}
.foot-col{top:1037px;font-size:11.8px;color:var(--footer-text);line-height:1.46}
.foot-col h3{font-size:15px;font-weight:700;color:#fff;margin-bottom:4px}
.foot-col li{list-style:none}
.foot-col li::before{content:"· ";color:var(--red)}
.social{left:729px;top:1063px;display:flex;gap:6px;align-items:center}
.social span{width:28px;height:28px;border-radius:4px}
.social .pill{width:40px;height:17px;border-radius:3px;background:#e9eef6;border:1px solid #aab}
</style>
</head>
<body>

<div class="abs topbar"></div>
<div class="abs lang">English<span class="lang-caret"></span></div>
<div class="abs field" style="left:427px;width:171px">Username</div>
<div class="abs field" style="left:603px;width:171px">•••••••</div>
<div class="abs btn btn-login">Login</div>
<div class="abs btn btn-signup">Sign Up</div>

<header class="abs header"></header>
<div class="abs logo"><span class="logo-mark"></span><span class="logo-name">Tarno Booking</span></div>
<nav class="abs nav">
  <span>About Tarno Booking</span><span>Videos</span><span>Documentation</span><span>Free Trial</span><span>Purchase</span><span>Compare</span>
</nav>

<section class="abs hero"></section>
<h1 class="abs heading hero-title">Introducing Tarno Booking</h1>
<p class="abs hero-copy">Tarno Booking is front office booking software which makes managing bookings, room and staff availability fast and simple. We focus on producing quality software which is powerful yet easy to use.</p>
<p class="abs hero-note">This is suitable for many types of business.</p>
<div class="abs cta">GET A FREE 3-MONTH TRIAL NOW »</div>

<div class="abs video">
  <svg class="abs video-play" width="32" height="40" viewBox="0 0 32 40"><path d="M2 2 L30 20 L2 38 Z" fill="#fff"/></svg>
  <div class="abs video-bar">
    <svg class="abs" style="left:9px;top:6px" width="9" height="10" viewBox="0 0 9 10"><path d="M0 0L9 5L0 10Z" fill="#333"/></svg>
    <div class="abs track"><i></i></div>
    <div class="abs knob"></div>
    <span class="abs" style="left:398px;top:5px">0:42/3:31</span>
    <svg class="abs" style="left:452px;top:5px" width="11" height="11" viewBox="0 0 11 11"><path d="M1 10L10 1M6 1h4v4M1 6v4h4" stroke="#333" fill="none" stroke-width="1.4"/></svg>
  </div>
</div>

<div class="abs feature" style="left:103px">
  <div class="feature-icon" role="img" aria-label="Stack of gold coins icon" style="background:linear-gradient(#f3d36a,#c99a22)"></div>
  <h2 class="heading feature-title">Low cost of ownership</h2>
  <p class="feature-text">Tarno Booking stores all data on our servers in the SaaS model giving a very low total cost of ownership our customers. You have zero investment in server platform hardware, zero investment in software licenses, zero investment in hardware and software upgrades, as these are included as part of the service.</p>
</div>
<div class="abs feature" style="left:386px">
  <div class="feature-icon" role="img" aria-label="Clipboard checklist icon" style="background:linear-gradient(#f2e7c8,#c9a46a)"></div>
  <h2 class="heading feature-title">Suitable for my business?</h2>
  <div class="feature-text">Tarno Booking works well with the following businesses:
    <ul>
      <li>Spa, Gym, Weight Management Center or Nail Salon</li>
      <li>Golf practice range with many tees for golfers to practive golf</li>
      <li>Room bookings (meeting, library &amp; computer rooms)</li>
      <li>Conference or meeting bookings</li>
      <li>Language teaching school, music school, educational center or general school</li>
    </ul>
  </div>
</div>
<div class="abs feature" style="left:659px">
  <svg class="feature-icon" viewBox="0 0 43 43" aria-hidden="true"><polygon points="13,1 30,1 42,13 42,30 30,42 13,42 1,30 1,13" fill="#c8181a"/><path d="M14 14L29 29M29 14L14 29" stroke="#fff" stroke-width="5" stroke-linecap="round"/></svg>
  <h2 class="heading feature-title">Drop the pen and paper</h2>
  <div class="feature-text">Tarno Booking is a professional booking software for day timetable bookings which out-performs pen and paper base booking systems and the common problems with them such as:
    <ul>
      <li>Difficult to move customer bookings</li>
      <li>Difficult to find all bookings for a single customer</li>
      <li>Difficult to find free times</li>
      <li>Spotting errors that may occur in a busy schedule</li>
    </ul>
  </div>
</div>

<div class="abs rule"></div>

<h2 class="abs heading section-title" style="left:103px;top:722px">Feature <em>Tour</em></h2>
<div class="abs tour">
  <div class="abs arrow" style="left:0;border-radius:0 28px 28px 0"><svg class="abs" style="left:6px;top:22px" width="10" height="12" viewBox="0 0 10 12"><path d="M8 1L3 6L8 11" stroke="#555" stroke-width="2" fill="none"/></svg></div>
  <div class="abs shot" style="left:47px">Screenshot</div>
  <div class="abs shot" style="left:287px">Screenshot</div>
  <div class="abs arrow" style="left:502px;border-radius:28px 0 0 28px"><svg class="abs" style="left:14px;top:22px" width="10" height="12" viewBox="0 0 10 12"><path d="M2 1L7 6L2 11" stroke="#555" stroke-width="2" fill="none"/></svg></div>
</div>

<h2 class="abs heading section-title" style="left:660px;top:722px">Latest <em>News</em></h2>
<article class="abs news" style="top:773px">
  <div class="news-date">11/10/2011</div>
  <div class="news-title">News title #01</div>
  <p class="news-body">It is a long established fact that a reader will be distracted by the readable content of a page when looking at its layout. <b>Read More »</b></p>
</article>
<div class="abs dots"></div>
<article class="abs news" style="top:880px">
  <div class="news-date">11/10/2011</div>
  <div class="news-title">News title #02</div>
  <p class="news-body">It is a long established fact that a reader will be distracted by the readable content of a page when looking at its layout. <b>Read More »</b></p>
</article>

<footer class="abs footer"></footer>
<div class="abs foot-logo"><span class="logo-mark"></span><span class="logo-name">Tarno Booking</span></div>
<div class="abs foot-copy">© 2011 Tarno Booking</div>
<div class="abs foot-col" style="left:311px">
  <h3>Links</h3>
  <ul>
    <li>About Tarno Booking</li><li>Videos</li><li>Documentation</li><li>Free Trial</li><li>Purchase</li><li>Compare</li><li>Terms and Conditions</li>
  </ul>
</div>
<div class="abs foot-col" style="left:520px">
  <h3>Contact Us</h3>
  <p>Email: hello@quenbel-works.example</p>
  <p>Phone: (852) 555-01742</p>
</div>
<div class="abs foot-col" style="left:729px"><h3>Get Social</h3></div>
<div class="abs social">
  <span style="background:#3b5a9a"></span>
  <span style="background:#3fb3e3"></span>
  <span style="background:#f08a1c"></span>
  <span class="pill"></span>
  <span class="pill" style="width:50px"></span>
</div>

</body>
</html>
```